Business card-Tales From The Harbor Gate

Looking for a business card. I have a website I designed "TalesFromTheHarborGate.com I am not a graphic artist and may at some point need help with my website too. Used the font "Hello Stockholm" on my website. I am a writer, looking to get published. Liked the "feel" of the cover below. No cliche typwriters, keyboards, pens. - Edgar P. Lindqvist
Updates

Not 100% sold on needing the owls, just a place to begin. I probably sounds like I'm going to be a pain to work with, I was a video production manager for 15+ years. When I would give an editor or graphic artist a project and let them run with it, the results were typically beyond my expectations. I give the idea then as the artists touch it, and adds value I could never bring to the project. Make something you would be proud of, don't try to second-guess me.

Target Market(s)

Agents, publishers, people I want to buy my book once I get it published

Industry/Entity Type

Publishing

Contact Information for Business Card

Edgar P. Lindqvist
TalesFromTheHarborGate.com
Phone #-TBD
Edgar@TalesFromTheHarbroGate.com
Maybe address; 418 N. 7th St Cheyenne, WY 82947

Colors
fcca95
3277b5

Requirements
Must have
• I like the "chromatic" feel of the attached cover. As you can see from my website, I'm an owl fan. Those pictures I took and do own the rights too. Not sure if they are approritae for a business card.
Should not have
• Cliche I like the "chromatic" feel of the attached book cover.
• I will need help with my website at some point too. I want the website to be easy for me to update, and reflect the same feel as the card. I write adventure, mystery. I have romance in my books too...Adventure of Romance, Romance of adventure, I am not sure but those words were like by an author firned of mine. They are rather "light" reading too.

```html
<!DOCTYPE html>
<html lang="en">
<head>
<meta charset="UTF-8">
<title>Tales From The Harbor Gate – Business Card</title>
<link rel="stylesheet" href="https://fonts.googleapis.com/css2?family=Allura&family=Montserrat:wght@400;500;600&display=swap">
<style>
  :root {
    --bg: #2b2b2d;
    --card: #ffffff;
    --ink-navy: #10223f;
    --ink-blue: #2e4d9b;
    --sky-blue: #a9cdea;
    --sky-pale: #dcecf8;
    --owl-brown: #6b5a3c;
    --owl-cream: #e9e6c9;
    --owl-blue: #9cb8c9;
  }
  * { margin: 0; padding: 0; box-sizing: border-box; }
  html, body {
    width: 1200px;
    height: 900px;
    overflow: hidden;
    background: var(--bg);
  }
  .stage {
    width: 1200px;
    height: 900px;
    display: flex;
    align-items: center;
    justify-content: center;
  }
  .business-card {
    position: relative;
    width: 1050px;
    height: 600px;
    background: var(--card);
    border-radius: 42px;
    overflow: hidden;
  }
  .sky-wash {
    position: absolute;
    left: 0;
    top: 0;
    width: 640px;
    height: 520px;
    background:
      radial-gradient(ellipse 260px 120px at 160px 150px, var(--sky-pale) 0%, transparent 70%),
      radial-gradient(ellipse 560px 380px at 40% 30%, var(--sky-blue) 0%, rgba(169,205,234,0.45) 45%, rgba(255,255,255,0) 80%);
  }
  .owl-photo {
    position: absolute;
    right: 0;
    top: 0;
    width: 500px;
    height: 540px;
    background:
      radial-gradient(ellipse 150px 120px at 45% 22%, var(--owl-cream) 0%, rgba(233,230,201,0) 100%),
      radial-gradient(ellipse 240px 260px at 58% 58%, var(--owl-brown) 0%, rgba(156,184,201,0.9) 55%, rgba(255,255,255,0) 100%),
      linear-gradient(160deg, #fbf6d8 0%, #f4f0c8 40%, #ffffff 100%);
    -webkit-mask-image: linear-gradient(to right, transparent 0%, #000 22%);
    mask-image: linear-gradient(to right, transparent 0%, #000 22%);
  }
  .contact-block {
    position: absolute;
    left: 90px;
    top: 110px;
    width: 560px;
    font-family: "Montserrat", sans-serif;
    color: var(--ink-navy);
  }
  .writer-name {
    font-family: "Allura", cursive;
    font-size: 84px;
    line-height: 1;
    color: var(--ink-navy);
    margin-left: 70px;
    white-space: nowrap;
  }
  .writer-role {
    font-family: "Allura", cursive;
    font-size: 62px;
    line-height: 1;
    color: var(--ink-blue);
    margin-left: 150px;
    margin-top: 2px;
  }
  .website {
    font-size: 38px;
    font-weight: 500;
    letter-spacing: 0.3px;
    margin-top: 28px;
    white-space: nowrap;
  }
  .email {
    font-size: 22px;
    color: var(--ink-blue);
    margin-top: 4px;
    margin-left: 60px;
    white-space: nowrap;
  }
  .phone {
    font-size: 32px;
    font-weight: 500;
    letter-spacing: 1px;
    margin-top: 22px;
    margin-left: 150px;
  }
  .address {
    font-size: 22px;
    font-weight: 500;
    margin-top: 8px;
    margin-left: 90px;
    white-space: nowrap;
  }
</style>
</head>
<body>
  <main class="stage">
    <section class="business-card">
      <div class="sky-wash"></div>
      <div class="owl-photo" role="img" aria-label="Photograph of a small owl perched, looking at the viewer"></div>
      <div class="contact-block">
        <p class="writer-name">Edgar P. Lindqvist</p>
        <p class="writer-role">Writer</p>
        <p class="website">TalesFromTheHarborGate.com</p>
        <p class="email">Edgar@TalesFromTheHarbroGate.com</p>
        <p class="phone">0555-2817-6390</p>
        <p class="address">418 N. 7th St Cheyenne, WY 82947</p>
      </div>
    </section>
  </main>
</body>
</html>
```